Construction APP

We need to design a modern app IOS/Android where my team can create a profile with their info, (maybe share some pictures), reviews, submit time cards, show their availability, etc.

Like a taxi app but for construction. We also want to be able to assign each team member to a project manager with who they currently working. So we will also need to be able to create profiles at the Administration level.

The goal is to keep innovating the app as we grow, so we are always open to suggestions and ideas.

Low design quality

Industry/Entity Type

Construction

Colors
FFC000
F8CF3A
FAE287
FDF2CF
FEFAEE

Requirements
Must have
• IOS/Android APP where my team can create a profile with their info, (maybe share some pictures), reviews, submit time cards, show their availability, etc.We also want to be able to assign each team member to a project manager with who they currently working. So we will also need to be able to create profiles at the Administration level.

```html
<!DOCTYPE html>
<html lang="en">
<head>
<meta charset="utf-8">
<title>Castellan Crew App Screens</title>
<link rel="stylesheet" href="https://fonts.googleapis.com/css2?family=Oswald:wght@500;600&family=Lato:ital,wght@0,400;0,700;1,400&display=swap">
<style>
  :root {
    --stage: #a9a9a9;
    --yellow: #f8cf3a;
    --gold: #e6b400;
    --cream-1: #fdf2cf;
    --cream-2: #fefaee;
    --cream-3: #fae287;
    --ink: #111111;
    --text: #333333;
    --muted: #555555;
    --line: #c9c9c9;
    --card: #f1f1f1;
    --white: #ffffff;
  }
  * { box-sizing: border-box; margin: 0; padding: 0; }
  html, body { width: 1200px; height: 557px; overflow: hidden; background: var(--stage); }
  body { position: relative; font-family: "Lato", sans-serif; color: var(--text); }

  .screen { position: absolute; top: 29px; width: 271px; overflow: hidden;
    background: linear-gradient(160deg, var(--cream-1) 0%, var(--cream-2) 55%, var(--cream-1) 100%); }
  .screen--welcome { left: 23px; height: 384px; }
  .screen--login { left: 316px; height: 384px; }
  .screen--profile { left: 609px; height: 483px; }
  .screen--reviews { left: 901px; height: 483px; }
  .abs { position: absolute; }
  .frame-note { position: absolute; right: 6px; bottom: 5px; font-size: 9px; color: var(--ink); }

  .brand { font-family: "Oswald", sans-serif; font-weight: 600; color: var(--ink); white-space: nowrap; letter-spacing: -0.3px; }
  .heading { font-family: "Oswald", sans-serif; font-weight: 600; color: var(--ink); letter-spacing: 0.4px; }
  .rule { position: absolute; height: 2px; width: 67px; background: var(--yellow); }
  .pill { position: absolute; border-radius: 20px; background: var(--yellow); color: var(--white);
    display: flex; align-items: center; justify-content: center; }

  /* welcome */
  .welcome-brand { left: 0; width: 100%; top: 150px; text-align: center; font-size: 29px; }
  .welcome-brand .dot { display: inline-block; width: 10px; height: 10px; border-radius: 50%; background: var(--gold); margin-right: 6px; vertical-align: middle; }
  .tagline { left: 20px; right: 20px; top: 199px; text-align: center; font-style: italic; font-size: 11.5px; line-height: 17px; color: #444; }
  .enter-btn { left: 86px; top: 266px; width: 100px; height: 33px; font-family: "Oswald", sans-serif; font-size: 12px; font-weight: 500; }

  /* login */
  .login-title { left: 10px; top: 52px; font-size: 23px; line-height: 26px; }
  .field { position: absolute; left: 11px; width: 248px; height: 34px; border-radius: 17px; background: var(--white);
    font-size: 9.5px; color: var(--muted); padding-left: 14px; display: flex; align-items: center; }
  .signup-btn { left: 11px; top: 225px; width: 248px; height: 34px; font-family: "Oswald", sans-serif; font-size: 12px; font-weight: 500; }
  .login-links { left: 0; width: 100%; top: 275px; text-align: center; font-size: 9.5px; color: var(--muted); }
  .login-links strong { color: #333; font-weight: 700; }

  /* inner screens */
  .top-brand { left: 11px; top: 47px; font-size: 14px; }
  .back-link { right: 11px; top: 32px; font-family: "Oswald", sans-serif; font-weight: 500; font-size: 11.5px; color: var(--ink); display: flex; align-items: center; gap: 6px; }
  .sheet { position: absolute; left: 0; right: 0; top: 77px; bottom: 0; background: var(--white); border-top-left-radius: 30px; }
  .sheet-title { left: 11px; top: 17px; font-size: 22px; }

  .avatar { left: 11px; top: 77px; width: 62px; height: 62px; border-radius: 3px;
    background: linear-gradient(180deg, #cfcac4 0%, #a58a7a 60%, #6d2a2a 100%); }
  .camera { left: 61px; top: 125px; width: 24px; height: 24px; border-radius: 50%; background: var(--yellow);
    display: flex; align-items: center; justify-content: center; }
  .user-name { left: 86px; top: 98px; font-size: 13px; }
  .edit-icon { left: 245px; top: 100px; }

  .menu { position: absolute; left: 11px; width: 248px; top: 166px; list-style: none; }
  .menu li { height: 33px; display: flex; align-items: center; justify-content: space-between;
    font-size: 9.5px; color: #333; border-bottom: 1px solid var(--line); padding-right: 4px; }
  .menu li:last-child { border-bottom: none; }

  .review { position: absolute; left: 11px; width: 248px; height: 82px; background: var(--card); border-radius: 5px; }
  .review-photo { position: absolute; left: 9px; top: 10px; width: 62px; height: 62px; border-radius: 3px; }
  .review-text { position: absolute; left: 83px; top: 8px; right: 8px; font-style: italic; font-size: 10px; line-height: 15.5px; color: #555; }
  .review-name { display: block; font-style: normal; font-size: 11px; color: var(--gold); margin-top: 1px; }
  .load-btn { left: 93px; top: 356px; width: 86px; height: 30px; font-size: 10.5px; font-weight: 700; }
</style>
</head>
<body>

<section class="screen screen--welcome">
  <div class="abs brand welcome-brand"><span class="dot"></span>MR. CASTELLAN</div>
  <p class="abs tagline">Sed ut perspiciatis unde omnis iste natus error sit voluptatem accusantium doloremque laudantium.</p>
  <div class="pill enter-btn">ENTER</div>
  <span class="frame-note">X10</span>
</section>

<section class="screen screen--login">
  <h1 class="abs heading login-title">LOG IN<br>CASTELLAN</h1>
  <div class="rule" style="left:12px;top:116px"></div>
  <div class="field" style="top:138px">Enter Email Address</div>
  <div class="field" style="top:181px">Enter Password</div>
  <div class="pill signup-btn">SIGN UP</div>
  <p class="abs login-links">Forgot Password? &nbsp;| &nbsp;<strong>Already Account</strong></p>
  <span class="frame-note">X10</span>
</section>

<section class="screen screen--profile">
  <div class="abs brand top-brand">MR. CASTELLAN</div>
  <div class="abs back-link"><svg width="5" height="8" viewBox="0 0 5 8"><path d="M4 1 1 4l3 3" fill="none" stroke="#111" stroke-width="1.5"/></svg>BACK</div>
  <div class="sheet">
    <h2 class="abs heading sheet-title">USER PROFILE</h2>
    <div class="rule" style="left:12px;top:57px"></div>
    <div class="abs avatar" role="img" aria-label="Profile photo of the team member"></div>
    <div class="abs camera"><svg width="11" height="9" viewBox="0 0 11 9"><rect x="0.5" y="1.5" width="10" height="7" rx="1" fill="#fff"/><rect x="3.5" y="0" width="4" height="2" fill="#fff"/><circle cx="5.5" cy="5" r="2" fill="#f8cf3a"/></svg></div>
    <div class="abs heading user-name">USER NAME</div>
    <svg class="abs edit-icon" width="11" height="11" viewBox="0 0 11 11"><path d="M1 10l.6-2.6L8 1l2 2-6.4 6.4z" fill="#f8cf3a"/></svg>
    <ul class="menu">
      <li>Password Reset<svg width="5" height="8" viewBox="0 0 5 8"><path d="M1 1l3 3-3 3" fill="none" stroke="#222" stroke-width="1.5"/></svg></li>
      <li>Edit Email Address<svg width="5" height="8" viewBox="0 0 5 8"><path d="M1 1l3 3-3 3" fill="none" stroke="#222" stroke-width="1.5"/></svg></li>
      <li>Account Settings<svg width="5" height="8" viewBox="0 0 5 8"><path d="M1 1l3 3-3 3" fill="none" stroke="#222" stroke-width="1.5"/></svg></li>
      <li>Availability<svg width="9" height="9" viewBox="0 0 9 9"><rect x="0" y="1.5" width="9" height="7.5" fill="#222"/><rect x="2" y="0" width="1" height="2" fill="#222"/><rect x="6" y="0" width="1" height="2" fill="#222"/><rect x="0.8" y="3.5" width="7.4" height="0.6" fill="#fff"/></svg></li>
      <li>Submit Time Cards</li>
      <li>Log out<svg width="5" height="8" viewBox="0 0 5 8"><path d="M1 1l3 3-3 3" fill="none" stroke="#222" stroke-width="1.5"/></svg></li>
    </ul>
    <span class="frame-note">X10</span>
  </div>
</section>

<section class="screen screen--reviews">
  <div class="abs brand top-brand">MR. CASTELLAN</div>
  <div class="abs back-link"><svg width="5" height="8" viewBox="0 0 5 8"><path d="M4 1 1 4l3 3" fill="none" stroke="#111" stroke-width="1.5"/></svg>BACK</div>
  <div class="sheet">
    <h2 class="abs heading sheet-title">CUSTOMER REVIEWS</h2>
    <div class="rule" style="left:12px;top:57px"></div>

    <article class="review" style="top:78px">
      <div class="review-photo" role="img" aria-label="Reviewer photo" style="background:linear-gradient(180deg,#9a9a9a,#5a5f68 60%,#1f3a5a)"></div>
      <p class="review-text">“ Sed ut perspiciatis unde omnis iste natus error sit &nbsp;voluptatem accusantium doloremque..”<span class="review-name">Name Heading</span></p>
    </article>
    <article class="review" style="top:171px">
      <div class="review-photo" role="img" aria-label="Reviewer photo" style="background:linear-gradient(180deg,#e6e6e6,#b89a88 55%,#2a2a2a)"></div>
      <p class="review-text">“ Sed ut perspiciatis unde omnis iste natus error sit &nbsp;voluptatem accusantium doloremque..”<span class="review-name">Name Heading</span></p>
    </article>
    <article class="review" style="top:263px">
      <div class="review-photo" role="img" aria-label="Reviewer photo" style="background:linear-gradient(180deg,#dcdcdc,#c4957c 55%,#f2f2f2)"></div>
      <p class="review-text">“ Sed ut perspiciatis unde omnis iste natus error sit &nbsp;voluptatem accusantium doloremque..”<span class="review-name">Name Heading</span></p>
    </article>

    <div class="pill load-btn">Load More</div>
    <span class="frame-note">X10</span>
  </div>
</section>

</body>
</html>
```